On Demand Digital Interview Lunch and Learn Event Flyer

We are hosting a lunch and learn for prospects to introduce our Digital Interview process - attendees are Human Resource and Hiring Managers.

We need a flyer that we can email and also have printed (large postcard size) to be either mailed out or dropped off at a prospects location. I have included a picture of a Digital Interview to be used on the flyer (people don't get it till they see it) as well as content. Please feel free to rewrite, restructure, the content to produce a good flow.

Return address on the back (the one we would print) is RL Workforce - 2740 Halden Road - Suite 318 - Nashville, TN 37482

Target Market(s)

Business Owners, Human Resource Managers

Industry/Entity Type

Digital

Font styles to use
Sans Serif

Requirements
Must have
• Must be clean and professional with plenty of white space

```html
<!DOCTYPE html>
<html lang="en">
<head>
<meta charset="utf-8">
<title>RL Workforce – Digital Interviews Lunch and Learn</title>
<link rel="stylesheet" href="https://fonts.googleapis.com/css2?family=Arimo:wght@400;700&family=Oswald:wght@500&display=swap">
<style>
  :root {
    --red: #d2232a;
    --black: #141414;
    --ink: #1d1d1d;
    --white: #ffffff;
    --backdrop: #e6e6e6;
    --photo-light: #f3f5f7;
    --photo-shirt: #b9cde3;
    --photo-screen: #3b4650;
    --photo-room: #dfe6ec;
    --placeholder-line: rgba(60, 80, 100, 0.28);
  }
  * { box-sizing: border-box; margin: 0; padding: 0; }
  html, body {
    width: 1200px; height: 800px; overflow: hidden;
    background: var(--backdrop);
    font-family: "Arimo", Arial, sans-serif;
    color: var(--ink);
  }
  .flyer {
    position: absolute; left: 120px; top: 90px;
    width: 960px; height: 620px;
    background: var(--white);
    overflow: hidden;
  }
  .hero-photo {
    position: absolute; left: 0; top: 0; width: 960px; height: 342px;
    background:
      linear-gradient(90deg,
        var(--photo-light) 0%,
        var(--photo-light) 12%,
        var(--photo-shirt) 30%,
        #9fb6cf 44%,
        var(--photo-room) 50%,
        var(--photo-screen) 56%,
        #6f7f8c 70%,
        var(--photo-screen) 80%,
        var(--photo-shirt) 90%,
        #c8d8ea 100%);
  }
  .hero-photo svg { position: absolute; inset: 0; width: 100%; height: 100%; }
  .brand {
    position: absolute; left: 42px; top: 226px;
  }
  .brand-name {
    font-size: 48px; font-weight: 700; color: var(--red);
    line-height: 1; letter-spacing: -0.5px;
  }
  .brand-tagline {
    margin-top: 10px; font-size: 13px; color: var(--ink);
  }
  .title-band {
    position: absolute; left: 0; top: 318px; width: 960px; height: 112px;
  }
  .headline {
    position: absolute; left: 45px; top: 338px;
    color: var(--white); font-size: 36.5px; line-height: 44px;
    font-weight: 400; text-transform: uppercase; letter-spacing: 0;
  }
  .headline strong { font-weight: 700; }
  .web-address {
    position: absolute; left: 711px; top: 376px;
    color: var(--red); font-size: 21px; font-weight: 700;
  }
  .intro {
    position: absolute; left: 45px; top: 456px; width: 522px;
    font-size: 15.5px; line-height: 19px; text-align: justify;
  }
  .details {
    position: absolute; left: 618px; top: 452px; width: 330px;
    list-style: none;
  }
  .detail { display: flex; align-items: flex-start; margin-bottom: 16px; }
  .detail-label {
    flex: 0 0 92px; height: 29px; padding-left: 12px;
    background: var(--red); color: var(--white);
    font-family: "Oswald", "Arial Narrow", sans-serif; font-weight: 500;
    font-size: 21px; line-height: 29px; text-transform: uppercase;
    clip-path: polygon(0 0, 100% 0, 93% 100%, 0 100%);
  }
  .detail-value {
    margin-left: 10px; font-size: 15px; line-height: 17px; margin-top: -1px;
  }
  .detail-value .phone { color: var(--red); font-weight: 700; }
</style>
</head>
<body>
  <main class="flyer">
    <div class="hero-photo" role="img" aria-label="Photo placeholder: three colleagues at a desk reviewing a recorded digital video interview on a computer monitor">
      <svg viewBox="0 0 960 342" preserveAspectRatio="none" aria-hidden="true">
        <rect x="1" y="1" width="958" height="340" fill="none" stroke="var(--placeholder-line)" stroke-width="2"/>
        <line x1="0" y1="0" x2="960" y2="342" stroke="var(--placeholder-line)" stroke-width="1.5"/>
        <line x1="960" y1="0" x2="0" y2="342" stroke="var(--placeholder-line)" stroke-width="1.5"/>
      </svg>
    </div>

    <div class="brand">
      <div class="brand-name">RL Workforce</div>
      <div class="brand-tagline">helping you find the perfect fit since 1986.</div>
    </div>

    <svg class="title-band" viewBox="0 0 960 112" aria-hidden="true">
      <polygon points="650,24 960,24 960,112 650,112" fill="var(--black)"/>
      <polygon points="0,0 676,0 700,112 0,112" fill="var(--red)"/>
    </svg>

    <h1 class="headline">How <strong>Digital Interviews</strong> Can<br>Produce <strong>Better Candidates</strong></h1>
    <div class="web-address">www.rlworkforce.com</div>

    <p class="intro">On Demand <strong>Digital Interviews</strong> offer individuals the ability to share their stories and demonstrate their work through video – all on their own time by using a PC, Mac, or Smartphone. More than 60% of interviews take place outside of the normal 9-5 business hours. Learn how Hiring Managers can save time, qualify more candidates, and can get a better overall first impression before setting up a first round interview.</p>

    <ul class="details">
      <li class="detail">
        <span class="detail-label">Where</span>
        <span class="detail-value">Linwood County Chamber<br>of Commerce</span>
      </li>
      <li class="detail">
        <span class="detail-label">When</span>
        <span class="detail-value">11:30 - 1:00pm<br>Wednesday, August 24th</span>
      </li>
      <li class="detail">
        <span class="detail-label">RSVP</span>
        <span class="detail-value">Dana.morrow@rlworkforce.com<br>or call <span class="phone">615 555-0142</span> for more<br>information.</span>
      </li>
    </ul>
  </main>
</body>
</html>
```